Property developer, money partner needs business card design using logo concept provided

Our company develops residential properties, does money lends for joint ventures in property deals and finds property deals for other money partners. We have provided a basic logo for you to work from. Any graphic or logo design on the card is to communicate development and finance collaboration. Color choice is not so important for us, but color choice does need to reflect professionalism.

```html
<!DOCTYPE html>
<html lang="en">
<head>
<meta charset="utf-8">
<title>Keystone Property Partners – Business Card</title>
<link rel="stylesheet" href="https://fonts.googleapis.com/css2?family=Montserrat:wght@400;500;600;700&display=swap">
<style>
  :root {
    --bg: #d9d9d9;
    --blue-light: #5ba8d8;
    --blue: #0670b8;
    --navy: #1a3c7a;
    --navy-deep: #203f7e;
    --card-white: #f1f1f1;
    --text-grey: #4a4a4a;
    --accent-red: #b5323a;
  }
  * { box-sizing: border-box; margin: 0; padding: 0; }
  html, body { width: 1200px; height: 1200px; overflow: hidden; }
  body {
    background: var(--bg);
    font-family: "Montserrat", sans-serif;
    position: relative;
  }
  .card {
    position: absolute;
    left: 150px;
    width: 900px;
    height: 514px;
    border-radius: 28px;
    overflow: hidden;
    box-shadow: 0 6px 18px rgba(0,0,0,.18);
  }
  .card-front {
    top: 52px;
    background: linear-gradient(90deg, var(--blue-light) 0%, #2d8cc9 40%, var(--blue) 75%);
    display: flex;
    flex-direction: column;
    align-items: center;
    justify-content: center;
    color: #fff;
  }
  .brand {
    display: flex;
    align-items: center;
    gap: 14px;
  }
  .brand-dot {
    width: 30px; height: 30px; border-radius: 50%;
    background: currentColor;
  }
  .brand-name {
    font-weight: 600;
    font-size: 30px;
    letter-spacing: 3px;
    text-transform: uppercase;
  }
  .brand-reg {
    margin-top: 12px;
    font-size: 13px;
    letter-spacing: 3px;
  }
  .card-back {
    top: 634px;
    background: var(--card-white);
    color: var(--text-grey);
  }
  .card-back .brand {
    position: absolute;
    left: 60px; top: 70px;
    color: var(--navy);
  }
  .card-back .brand-dot { width: 22px; height: 22px; }
  .card-back .brand-name { font-size: 20px; letter-spacing: 2px; }
  .card-back .brand-reg {
    position: absolute; left: 96px; top: 104px; margin: 0;
    font-size: 10px; color: var(--text-grey);
  }
  .person {
    position: absolute; right: 60px; top: 150px; text-align: right;
  }
  .person-name {
    font-size: 42px; font-weight: 700; color: var(--navy); line-height: 1.1;
  }
  .person-role { font-size: 21px; margin-top: 6px; }
  .divider {
    position: absolute; left: 120px; top: 268px;
    width: 520px; height: 2px; background: var(--blue);
  }
  .address {
    position: absolute; right: 60px; top: 260px;
    text-align: right; font-size: 22px; line-height: 1.45;
  }
  .contacts {
    position: absolute; left: 60px; top: 300px;
    list-style: none; font-size: 22px; line-height: 1.6;
  }
  .contacts li { display: flex; align-items: center; gap: 16px; }
  .contacts svg { width: 22px; height: 22px; fill: var(--navy); flex: none; }
  .bands { position: absolute; left: 0; bottom: 0; width: 900px; height: 80px; }
</style>
</head>
<body>
  <section class="card card-front">
    <div class="brand">
      <span class="brand-dot"></span>
      <span class="brand-name">Keystone Property Partners</span>
    </div>
    <p class="brand-reg">A.C.N 318 204 759</p>
  </section>

  <section class="card card-back">
    <div class="brand">
      <span class="brand-dot"></span>
      <span class="brand-name">Keystone Property Partners</span>
    </div>
    <p class="brand-reg">A.C.N 318 204 759</p>

    <div class="person">
      <h1 class="person-name">Marcus Avery</h1>
      <p class="person-role">Founder &amp; Director</p>
    </div>

    <div class="divider"></div>

    <address class="address">4178 Alder Road<br>Bayfield Maine 11406</address>

    <ul class="contacts">
      <li>
        <svg viewBox="0 0 24 24"><path d="M6.6 10.8a15.1 15.1 0 0 0 6.6 6.6l2.2-2.2c.3-.3.7-.4 1-.2 1.1.4 2.3.6 3.6.6.6 0 1 .4 1 1V20c0 .6-.4 1-1 1A17 17 0 0 1 3 4c0-.6.4-1 1-1h3.5c.6 0 1 .4 1 1 0 1.3.2 2.5.6 3.6.1.3 0 .7-.2 1z"/></svg>
        (405)-555-0142
      </li>
      <li>
        <svg viewBox="0 0 24 24"><path d="M2 5h20v14H2z M2 5l10 8 10-8" /></svg>
        hello@keystonepartners.co
      </li>
      <li>
        <svg viewBox="0 0 24 24"><path d="M12 2a10 10 0 1 0 0 20 10 10 0 0 0 0-20zm6.9 9h-3a15 15 0 0 0-1.4-6A8 8 0 0 1 18.9 11zM12 4c.9 1.2 1.8 3.6 2 7h-4c.2-3.4 1.1-5.8 2-7zM4.1 13h3a15 15 0 0 0 1.4 6A8 8 0 0 1 4.1 13zm3-2h-3a8 8 0 0 1 4.4-6 15 15 0 0 0-1.4 6zM12 20c-.9-1.2-1.8-3.6-2-7h4c-.2 3.4-1.1 5.8-2 7zm3.5-1a15 15 0 0 0 1.4-6h3a8 8 0 0 1-4.4 6z"/></svg>
        www.keystonepartners.co
      </li>
    </ul>

    <svg class="bands" viewBox="0 0 900 80" preserveAspectRatio="none" aria-hidden="true">
      <polygon points="0,58 450,8 420,80 0,80" fill="var(--navy-deep)"/>
      <polygon points="478,8 900,8 900,80 446,80" fill="var(--blue)"/>
    </svg>
  </section>
</body>
</html>
```